QWTORAMX ( Wordpress website for catalogue of Zintrop Cast Pages)

Need a website to showcase different Zintrop Cast pages ( in different categories). Similar to e-commerce except no check-out / purchase of items. Pls use our logos provided and color scheme to be white+red+ blue as per our logo.

Target Market(s)

Consumers

Font styles to use
Sans Serif

Colors
ffffff
ec1f27
3276b5

Requirements
Must have
• I will need a Wordpress Theme as a handover. Also, pls use the color scheme (red+blue+white) as per logo attached. Prefer clean and near design with white space.

```html
<!DOCTYPE html>
<html lang="en">
<head>
<meta charset="utf-8">
<title>QWTORAMX – A Portal of Curated Zintrop Cast</title>
<link rel="stylesheet" href="https://fonts.googleapis.com/css2?family=Oswald:wght@700&family=Montserrat:wght@700;800&family=Roboto:wght@400;500;700&family=Pacifico&display=swap">
<style>
:root{
  --red:#ec1f27;
  --blue:#3276b5;
  --blue-light:#5b93c9;
  --white:#ffffff;
  --ink:#222222;
  --grey:#555555;
  --ring-red:#fde0e1;
  --ring-blue:#dbe7f4;
}
*{box-sizing:border-box;margin:0;padding:0}
html,body{width:1200px;height:2982px;overflow:hidden;background:var(--white)}
body{position:relative;font-family:"Roboto",sans-serif;color:var(--ink)}
.abs{position:absolute}

/* brand mark */
.brand{position:absolute;display:flex;align-items:center;gap:8px;font-family:"Roboto",sans-serif;font-weight:700;color:var(--blue);letter-spacing:.5px}
.brand .dot{background:var(--red);flex:none}
.brand-header{left:142px;top:26px;font-size:36px}
.brand-header .dot{width:14px;height:14px}

/* navigation */
.nav{position:absolute;top:38px;left:433px;display:flex;font-size:14px;color:#333}
.nav a{color:inherit;text-decoration:none;margin-right:26px;position:relative;padding-bottom:10px}
.nav a.active::after{content:"";position:absolute;left:-4px;right:-4px;bottom:0;height:3px;background:var(--blue)}
.btn{position:absolute;background:var(--red);color:var(--white);font-family:"Roboto",sans-serif;font-weight:700;display:flex;align-items:center;justify-content:center;text-decoration:none}
.btn-header{left:962px;top:28px;width:93px;height:38px;font-size:16px}

/* hero */
.hero-art{left:440px;top:150px;width:742px;height:360px;border-radius:40px 120px 20px 20px;background:linear-gradient(120deg,#eef2fb 0%,#d9e4f6 45%,#f3d6d9 100%)}
.hero-title{position:absolute;z-index:2;left:52px;top:228px;font-family:"Oswald",sans-serif;font-weight:700;font-size:80px;line-height:66px;color:var(--ink);text-transform:uppercase;letter-spacing:-1px}
.hero-title .of{position:absolute;left:286px;top:30px;font-family:"Pacifico",cursive;font-size:60px;line-height:80px;color:var(--red);text-transform:none;letter-spacing:0;white-space:nowrap}
.hero-title .tag{display:inline-block;margin-top:12px;background:var(--red);color:var(--white);padding:0 14px;line-height:60px;font-size:64px;border-radius:4px}
.stripe{left:0;top:544px;width:1200px;height:12px;background:linear-gradient(100deg,var(--red) 0 46%,var(--blue) 46% 100%)}

/* member call */
.member{position:absolute;left:141px;top:614px;font-family:"Montserrat",sans-serif;font-weight:800;font-size:36px;color:var(--ink);letter-spacing:.5px}
.btn-member{left:936px;top:611px;width:119px;height:50px;font-size:20px}

/* quick links */
.quick{position:absolute;top:740px;left:143px;display:flex;gap:53px}
.quick-item{width:140px;text-align:center}
.quick-ring{width:140px;height:140px;border-radius:50%;display:flex;align-items:center;justify-content:center}
.quick-ring .core{width:110px;height:110px;border-radius:50%;display:flex;align-items:center;justify-content:center}
.is-blue .quick-ring{background:var(--ring-blue)} .is-blue .core{background:var(--blue)}
.is-red .quick-ring{background:var(--ring-red)} .is-red .core{background:var(--red)}
.quick-label{margin-top:15px;font-size:19px;font-weight:500;color:var(--ink)}

/* catalogue grid */
.grid{position:absolute;left:142px;top:996px;display:grid;grid-template-columns:452px 452px;grid-auto-rows:348px;column-gap:9px;row-gap:9px}
.card{position:relative;border:1px solid #e2e2e2;border-radius:4px;padding:7px;background:var(--white)}
.card .photo{width:100%;height:100%}
.card .badge{position:absolute;right:0;top:0;width:178px;height:52px;background:var(--white);border-radius:0 4px 0 6px;display:flex;align-items:center;justify-content:center;gap:7px;font-weight:700;font-size:24px;color:var(--blue)}
.card .badge .dot{width:10px;height:10px;background:var(--red)}
.p1{background:linear-gradient(135deg,#e9d8c6,#c97a4a 50%,#6f8f3c)}
.p2{background:linear-gradient(135deg,#d8d6d2,#8f8c88 55%,#4a4846)}
.p3{background:linear-gradient(135deg,#4e5a74,#b8b9c4 55%,#3a3a45)}
.p4{background:linear-gradient(135deg,#e7e1b8,#d8362c 45%,#3d3a30)}
.p5{background:linear-gradient(135deg,#e8cfd3,#4f6272 50%,#9aa0a4)}
.p6{background:linear-gradient(135deg,#d6d7d8,#f0b8c6 40%,#7cb6db 70%,#3b2b2e)}

/* contact */
.contact{left:0;top:2143px;width:1200px;height:683px;background:var(--blue);overflow:hidden}
.contact-title{position:absolute;left:168px;top:2218px;font-family:"Montserrat",sans-serif;font-weight:800;font-size:60px;color:var(--white);letter-spacing:1px}
.contact-intro{position:absolute;left:609px;top:2224px;width:450px;font-size:19px;line-height:29px;color:var(--white)}
.field{position:absolute;left:609px;width:427px;height:51px;border:1px solid rgba(255,255,255,.75);color:var(--white);font-size:14px;padding:17px 28px}
.btn-submit{left:609px;top:2691px;width:138px;height:48px;font-size:21px}
.contact-art{left:12px;top:2606px;width:486px;height:220px;border-radius:90px 90px 0 0;background:linear-gradient(120deg,#eef2fb,#c9d9f1 55%,#f1cdd1)}

/* footer */
.brand-footer{left:142px;top:2866px;font-size:62px;gap:12px}
.brand-footer .dot{width:22px;height:22px}
.legal{position:absolute;left:612px;top:2866px;font-size:15px;color:#333}
.legal span{margin:0 6px;color:#888}
.social{position:absolute;left:612px;top:2916px;display:flex;gap:19px}
.social i{width:40px;height:40px;border-radius:50%;background:#6f6f6f;display:flex;align-items:center;justify-content:center}
</style>
</head>
<body>

<header>
  <div class="brand brand-header"><span>QWTORAMX</span><span class="dot"></span></div>
  <nav class="nav">
    <a class="active">HOME</a><a>MY ACCOUNT</a><a>VIEW ORDERS</a><a>VIEW REWARDS</a><a>ABOUT US</a>
  </nav>
  <a class="btn btn-header">SIGN IN</a>
</header>

<section class="hero">
  <div class="abs hero-art" role="img" aria-label="Illustration of a phone showing a live shopping stream beside two cheerful shoppers carrying bags and boxes among groceries and clothing racks"></div>
  <h1 class="hero-title">A Portal<span class="of">Of</span><br>Curated<br>Zintrop<br><span class="tag">Cast</span></h1>
</section>
<div class="abs stripe"></div>

<section>
  <h2 class="member">NOT A MEMBER ? PLEASE SIGN IN NOW</h2>
  <a class="btn btn-member">SIGN IN</a>
</section>

<section class="quick">
  <div class="quick-item is-blue">
    <div class="quick-ring"><div class="core">
      <svg width="54" height="50" viewBox="0 0 54 50" fill="#fff"><path d="M2 4h9l7 27h27l6-20H16" fill="none" stroke="#fff" stroke-width="6" stroke-linejoin="round" stroke-linecap="round"/><rect x="18" y="14" width="28" height="13"/><circle cx="22" cy="42" r="5"/><circle cx="42" cy="42" r="5"/></svg>
    </div></div>
    <div class="quick-label">ORDERS</div>
  </div>
  <div class="quick-item is-red">
    <div class="quick-ring"><div class="core">
      <svg width="56" height="50" viewBox="0 0 56 50" fill="#fff"><path d="M6 17h12L44 4v40L18 31H6z"/><path d="M14 31h9l4 15h-9z"/><rect x="47" y="18" width="6" height="12" rx="3"/></svg>
    </div></div>
    <div class="quick-label">PROMOS</div>
  </div>
  <div class="quick-item is-blue">
    <div class="quick-ring"><div class="core">
      <svg width="48" height="48" viewBox="0 0 48 48" fill="#fff"><rect x="3" y="14" width="42" height="10"/><rect x="7" y="26" width="34" height="20"/><path d="M24 14c-4-10-14-10-14-4s10 4 14 4c4 0 14 2 14-4s-10-6-14 4z" fill="none" stroke="#fff" stroke-width="4"/><rect x="21" y="14" width="6" height="32" fill="#3276b5"/></svg>
    </div></div>
    <div class="quick-label">REWARDS</div>
  </div>
  <div class="quick-item is-red">
    <div class="quick-ring"><div class="core">
      <svg width="48" height="48" viewBox="0 0 48 48" fill="#fff"><path d="M10 3l9 10-5 7c3 6 8 11 14 14l7-5 10 9-6 8C22 44 4 26 2 10z"/></svg>
    </div></div>
    <div class="quick-label">CALL US</div>
  </div>
  <div class="quick-item is-blue">
    <div class="quick-ring"><div class="core">
      <svg width="40" height="52" viewBox="0 0 40 52" fill="#fff"><path d="M20 2C10 2 3 9 3 19c0 12 17 31 17 31s17-19 17-31C37 9 30 2 20 2zm0 24a7 7 0 1 1 0-14 7 7 0 0 1 0 14z"/></svg>
    </div></div>
    <div class="quick-label">DIRECTION</div>
  </div>
</section>

<section class="grid">
  <article class="card"><div class="photo p1" role="img" aria-label="Collage of meal deal promo cards with grilled food and price tags"></div><div class="badge">QWTORAMX<span class="dot"></span></div></article>
  <article class="card"><div class="photo p2" role="img" aria-label="Shelves stocked with boxed home gadgets and appliances"></div><div class="badge">QWTORAMX<span class="dot"></span></div></article>
  <article class="card"><div class="photo p3" role="img" aria-label="Store display of kitchen appliances, massagers and air fryers"></div><div class="badge">QWTORAMX<span class="dot"></span></div></article>
  <article class="card"><div class="photo p4" role="img" aria-label="Grid of fresh fruit boxes including tomatoes, grapes and mangoes"></div><div class="badge">QWTORAMX<span class="dot"></span></div></article>
  <article class="card"><div class="photo p5" role="img" aria-label="Fashion collage of dresses modelled in several colours"></div><div class="badge">QWTORAMX<span class="dot"></span></div></article>
  <article class="card"><div class="photo p6" role="img" aria-label="Grid of plush novelty headbands in pastel colours"></div><div class="badge">QWTORAMX<span class="dot"></span></div></article>
</section>

<section>
  <div class="abs contact">
    <svg width="1200" height="683" viewBox="0 0 1200 683">
      <path d="M565 0H600C555 175 400 330 0 330V290C380 290 520 150 565 0Z" fill="var(--blue-light)"/>
      <path d="M0 0H565C520 150 380 290 0 290Z" fill="var(--red)"/>
    </svg>
  </div>
  <h2 class="contact-title">CONTACT</h2>
  <p class="contact-intro">Feel free to contact us via Zintrop, Pixtagon, email or just Call us at 1 800 555 0199 for any enquiries.</p>
  <div class="field" style="top:2341px">Enter Name</div>
  <div class="field" style="top:2408px">Enter Email</div>
  <div class="field" style="top:2477px">Phone</div>
  <div class="field" style="top:2544px;height:125px">Message</div>
  <a class="btn btn-submit">SUBMIT</a>
  <div class="abs contact-art" role="img" aria-label="Small illustration of a phone with a live stream next to two shoppers with bags and goods"></div>
</section>

<footer>
  <div class="brand brand-footer"><span>QWTORAMX</span><span class="dot"></span></div>
  <p class="legal">© 2020 QWTORAMX . All Rights Reserved<span>|</span>Privacy Policy<span>|</span>Terms</p>
  <div class="social">
    <i></i><i></i><i></i>
    <i><svg width="18" height="14" viewBox="0 0 18 14" fill="none" stroke="#fff" stroke-width="1.6"><rect x="1" y="1" width="16" height="12" rx="1.5"/><path d="M1 2l8 6 8-6"/></svg></i>
  </div>
</footer>

</body>
</html>
```